Poster for a series of live music events

Looking for a simplistic poster design for live music gigs. I would like something that i can reuse by moving the positioning of the words on the poster and the colour scheme. Attached is an example of a design that i like. The size should be A4.
File format preferred would be photoshop.
Text in the poster is not that important at this stage as it is just a template i am after. But it should include band names, location, date and time. So feel free to make up the text. The file provided in the brief will show you the similar things that will be included.
Events

```html
<!DOCTYPE html>
<html lang="en">
<head>
<meta charset="utf-8">
<title>Fern &amp; Callum · Owen Hartley — Acoustic Session</title>
<link rel="stylesheet" href="https://fonts.googleapis.com/css2?family=Emilys+Candy&family=Bebas+Neue&family=Federo&family=Alfa+Slab+One&display=swap">
<style>
  :root {
    --rust-light: #b9561e;
    --rust-mid: #8a3512;
    --rust-dark: #3e1808;
    --slate-light: #5a5e4c;
    --slate-dark: #2c2e26;
    --moss-light: #6e8a2c;
    --moss-mid: #4a6420;
    --moss-dark: #28381a;
    --cream: #f6efa8;
    --cream-warm: #f3e4a0;
    --shadow: rgba(20, 10, 0, 0.75);
    --star: #f7e21a;
    --sand: #c9a27c;
    --ink: #0c0c0c;
    --white: #ffffff;
  }
  * { margin: 0; padding: 0; box-sizing: border-box; }
  html, body { width: 848px; height: 1200px; overflow: hidden; }
  body { background: var(--rust-dark); }

  .poster {
    position: relative;
    width: 848px;
    height: 1200px;
    overflow: hidden;
    background:
      radial-gradient(ellipse at 50% 45%, var(--rust-light) 0%, var(--rust-mid) 55%, var(--rust-dark) 100%);
  }

  .headline-panel {
    position: absolute;
    left: 38px; top: 22px;
    width: 770px; height: 386px;
    background: linear-gradient(160deg, var(--slate-light) 0%, var(--slate-dark) 60%, #3c3a30 100%);
    box-shadow: 0 4px 14px var(--shadow);
    border: 1px solid rgba(0,0,0,0.5);
  }
  .act {
    position: absolute;
    left: 0; width: 100%;
    text-align: center;
    font-family: "Emilys Candy", cursive;
    color: var(--cream);
    text-shadow: 3px 3px 2px var(--shadow);
    white-space: nowrap;
  }
  .act--support { top: 58px; font-size: 82px; }
  .act--headliner { top: 230px; font-size: 88px; }
  .star {
    position: absolute;
    top: 268px;
    width: 74px; height: 72px;
  }
  .star--left { left: 40px; }
  .star--right { left: 733px; }

  .session-band {
    position: absolute;
    top: 443px; left: 0; width: 100%; height: 66px;
  }
  .session-strip {
    position: absolute;
    top: 4px; height: 56px;
    background: linear-gradient(180deg, #d8b68e, var(--sand) 50%, #a8825e);
    box-shadow: 0 2px 6px var(--shadow);
  }
  .session-strip--left { left: 44px; width: 108px; }
  .session-strip--right { left: 694px; width: 110px; }
  .session-title {
    position: absolute;
    left: 0; width: 100%; top: 0;
    text-align: center;
    font-family: "Bebas Neue", sans-serif;
    font-size: 70px; line-height: 66px;
    letter-spacing: 2px;
    color: var(--cream-warm);
    text-shadow: 3px 3px 2px var(--shadow);
  }

  .details-panel {
    position: absolute;
    left: 46px; top: 528px;
    width: 750px; height: 470px;
    background:
      radial-gradient(ellipse at 35% 40%, var(--moss-light) 0%, var(--moss-mid) 50%, var(--moss-dark) 100%);
    box-shadow: 0 4px 14px var(--shadow);
    border: 1px solid rgba(0,0,0,0.5);
    font-family: "Federo", sans-serif;
    color: var(--cream);
  }
  .details-panel * { text-shadow: 3px 3px 2px var(--shadow); }
  .date {
    position: absolute;
    left: 52px; top: 50px;
    font-size: 84px; letter-spacing: 3px;
    word-spacing: 24px;
    white-space: nowrap;
  }
  .time {
    position: absolute;
    left: 50px; top: 222px;
    font-size: 42px; letter-spacing: 3px;
  }
  .venue-lead {
    position: absolute;
    left: 228px; top: 212px;
    font-family: "Alfa Slab One", serif;
    font-size: 26px; line-height: 34px;
    text-align: center;
  }
  .venue {
    position: absolute;
    left: 312px; top: 162px;
    width: 440px;
    font-family: "Alfa Slab One", serif;
    font-size: 70px; line-height: 88px;
    text-align: center;
    transform: scaleX(0.72);
    transform-origin: left top;
    white-space: nowrap;
  }
  .venue span { display: block; }
  .entry {
    position: absolute;
    left: 32px; top: 356px;
    white-space: nowrap;
  }
  .entry-price { font-size: 72px; }
  .entry-label { font-size: 50px; letter-spacing: 2px; margin-left: 10px; }

  .light-beam {
    position: absolute;
    left: 0; top: 0;
    width: 848px; height: 1200px;
    pointer-events: none;
  }

  .brand-art {
    position: absolute;
    left: 282px; top: 988px;
    width: 280px; height: 200px;
    border-radius: 50%;
    background: radial-gradient(ellipse at center, rgba(12,12,12,0.55) 0%, rgba(12,12,12,0.25) 50%, rgba(12,12,12,0) 72%);
  }
  .brand {
    position: absolute;
    left: 240px; top: 1076px;
    width: 308px; height: 44px;
    background: var(--ink);
    text-align: center;
    font-family: "Bebas Neue", sans-serif;
    font-size: 44px; line-height: 48px;
    letter-spacing: 2px;
    color: var(--white);
  }
</style>
</head>
<body>
<main class="poster">

  <section class="headline-panel">
    <h1 class="act act--support">Fern &amp; Callum</h1>
    <svg class="star star--left" viewBox="0 0 100 96" aria-hidden="true">
      <polygon points="50,2 62,36 98,37 69,58 80,93 50,72 20,93 31,58 2,37 38,36" fill="var(--star)" stroke="rgba(0,0,0,0.4)" stroke-width="2"/>
    </svg>
    <h2 class="act act--headliner">Owen Hartley</h2>
    <svg class="star star--right" viewBox="0 0 100 96" aria-hidden="true">
      <polygon points="50,2 62,36 98,37 69,58 80,93 50,72 20,93 31,58 2,37 38,36" fill="var(--star)" stroke="rgba(0,0,0,0.4)" stroke-width="2"/>
    </svg>
  </section>

  <div class="session-band">
    <span class="session-strip session-strip--left"></span>
    <p class="session-title">Acoustic Session</p>
    <span class="session-strip session-strip--right"></span>
  </div>

  <section class="details-panel">
    <p class="date">THURSDAY 23</p>
    <p class="time">8 PM</p>
    <p class="venue-lead">AT<br>THE</p>
    <p class="venue"><span>OLD HARLOW</span><span>FOUNDRY</span></p>
    <p class="entry"><span class="entry-price">£10</span><span class="entry-label">ENTRY</span></p>
  </section>

  <svg class="light-beam" viewBox="0 0 848 1200" aria-hidden="true">
    <defs>
      <linearGradient id="beam" x1="0" y1="0" x2="1" y2="1">
        <stop offset="0" stop-color="#fff6c8" stop-opacity="0.05"/>
        <stop offset="0.5" stop-color="#fff6c8" stop-opacity="0.55"/>
        <stop offset="1" stop-color="#fff6c8" stop-opacity="0"/>
      </linearGradient>
    </defs>
    <polygon points="600,930 720,930 470,1200 300,1200" fill="url(#beam)"/>
    <polygon points="420,990 520,990 330,1200 250,1200" fill="url(#beam)" opacity="0.7"/>
  </svg>

  <div class="brand-art" role="img" aria-label="Splash of musical notes and a treble clef behind the promoter name"></div>
  <p class="brand">loudhouse</p>

</main>
</body>
</html>
```